Vantor Advisory business card

Premium business card required
I have attached the brand as a powerpoint template but this can be made to look very up market, I have also attached my BIO for title reasons and to give you a feel for my skills
front of card
Derek Holloway
Managing Director Vantor Advisory
Retail, Customer-Led Experience, Transformation and Maximising Shareholder Return
Mobile +61(0)418557392
Email derekvantoradvisory.com
back of card

VANTOR ADVISORY’ OFFERING

We transform customer environments to extract benefits while elevating service levels;
We release millions of dollars in self-funding through continuous improvement;
We see CX as a key differentiator, proactively guarding share from market disrupters;
We re-invent service and create front-end of the future.

```html
<!DOCTYPE html>
<html lang="en">
<head>
<meta charset="utf-8">
<title>Vantor Advisory business card</title>
<link href="https://fonts.googleapis.com/css2?family=Montserrat:wght@600;700;800&family=Oswald:wght@200;600;700&family=Open+Sans:wght@600&display=swap" rel="stylesheet">
<style>
  :root {
    --bg: #e9e7e4;
    --ink-dark: #1e1612;
    --ink-dark-2: #2e231d;
    --gold: #e0b53a;
    --gold-deep: #b8831c;
    --gold-light: #f6d77a;
    --orange: #f6a418;
    --orange-light: #fcc24a;
    --orange-deep: #e58a06;
    --text-dark: #1a1410;
    --white: #ffffff;
  }
  * { margin: 0; padding: 0; box-sizing: border-box; }
  html, body { width: 1200px; height: 1000px; overflow: hidden; }
  body {
    background: var(--bg);
    display: flex;
    align-items: center;
    justify-content: center;
    gap: 40px;
  }
  .card {
    position: relative;
    width: 540px;
    height: 310px;
    overflow: hidden;
    box-shadow: 0 10px 30px rgba(0,0,0,.18);
  }
  .card-texture { position: absolute; inset: 0; }

  /* Front: brand side */
  .card--front .card-texture {
    background: radial-gradient(ellipse at 50% 35%, var(--ink-dark-2), var(--ink-dark) 75%);
  }
  .brand {
    position: absolute;
    top: 66px; left: 0; right: 0;
    display: flex; flex-direction: column; align-items: center;
  }
  .brand-lockup { display: flex; align-items: center; gap: 14px; }
  .brand-name {
    font-family: "Montserrat", sans-serif;
    font-weight: 800;
    font-size: 40px;
    letter-spacing: 1px;
    color: var(--gold);
    line-height: 1;
  }
  .brand-dot {
    width: 42px; height: 42px; border-radius: 50%;
    background: var(--gold);
  }
  .brand-tagline {
    margin-top: 14px;
    font-family: "Montserrat", sans-serif;
    font-weight: 700;
    font-size: 21px;
    color: var(--gold);
  }
  .gold-rule {
    position: absolute;
    left: 22px; right: 22px; top: 238px;
    height: 2px;
    background: linear-gradient(90deg, var(--gold-deep), var(--gold-light), var(--gold-deep));
  }
  .contact {
    position: absolute;
    top: 254px;
    display: flex; align-items: center; gap: 8px;
    font-family: "Open Sans", sans-serif;
    font-weight: 600;
    font-size: 17px;
    color: var(--white);
  }
  .contact--phone { left: 26px; }
  .contact--web { right: 26px; }
  .contact svg { width: 18px; height: 18px; }

  /* Back: offering side */
  .card--back .card-texture {
    background: linear-gradient(160deg, var(--orange-light), var(--orange) 45%, var(--orange-deep));
  }
  .person {
    position: absolute; top: 24px; left: 28px;
    font-family: "Oswald", sans-serif;
    color: var(--text-dark);
    text-transform: uppercase;
  }
  .person-name { font-size: 34px; line-height: 1; }
  .person-first { font-weight: 200; }
  .person-last { font-weight: 700; }
  .person-title {
    margin-top: 6px;
    padding-bottom: 6px;
    border-bottom: 2px solid var(--text-dark);
    font-weight: 600;
    font-size: 15px;
    letter-spacing: 3px;
  }
  .offering {
    position: absolute;
    top: 118px; left: 28px; right: 28px;
    font-family: "Oswald", sans-serif;
    color: var(--text-dark);
    text-transform: uppercase;
  }
  .offering-title {
    font-weight: 700;
    font-size: 17px;
    letter-spacing: .5px;
    text-align: right;
    margin-bottom: 10px;
  }
  .offering-list { list-style: none; }
  .offering-list li {
    font-weight: 600;
    font-size: 13px;
    line-height: 1.4;
    letter-spacing: .4px;
  }
</style>
</head>
<body>
  <section class="card card--front">
    <div class="card-texture" role="img" aria-label="Dark brown quilted diamond pattern background"></div>
    <div class="brand">
      <div class="brand-lockup">
        <span class="brand-name">VANTOR ADVISORY</span>
        <span class="brand-dot"></span>
      </div>
      <p class="brand-tagline">Retail Service Transformation</p>
    </div>
    <div class="gold-rule"></div>
    <p class="contact contact--phone">
      <svg viewBox="0 0 24 24" aria-hidden="true"><path fill="#e0b53a" d="M6.6 10.8a15.1 15.1 0 0 0 6.6 6.6l2.2-2.2a1 1 0 0 1 1-.25 11.4 11.4 0 0 0 3.6.57 1 1 0 0 1 1 1V20a1 1 0 0 1-1 1A17 17 0 0 1 3 4a1 1 0 0 1 1-1h3.5a1 1 0 0 1 1 1c0 1.250.2 2.450.57 3.570a1 1 0 0 1-.25 1z"/></svg>
      +61(0)418557392
    </p>
    <p class="contact contact--web">
      <svg viewBox="0 0 24 24" aria-hidden="true"><rect x="2" y="5" width="20" height="14" fill="#e0b53a"/><path d="M2 5l10 8 10-8M2 19l8-7M22 19l-8-7" stroke="#1e1612" stroke-width="1.5" fill="none"/></svg>
      derekvantoradvisory.com
    </p>
  </section>

  <section class="card card--back">
    <div class="card-texture" role="img" aria-label="Golden orange quilted diamond pattern background"></div>
    <div class="person">
      <p class="person-name"><span class="person-first">Derek</span> <span class="person-last">Holloway</span></p>
      <p class="person-title">Managing Director</p>
    </div>
    <div class="offering">
      <h2 class="offering-title">Vantor Advisory’ Offering</h2>
      <ul class="offering-list">
        <li>We transform customer environments to extract benefits while elevating service levels.</li>
        <li>We release millions of dollars in self-funding through continuous improvement.</li>
        <li>We see CX as a key differentiator proactively guarding share from market disrupters.</li>
      </ul>
    </div>
  </section>
</body>
</html>
```